Business Card Design Project- Removalist

I would like to surprise my husband to be with a different type of wedding present. His brother (who he owned a removalist business with) suddenly passed away from cancer recently and he has changed his business name to 'RTB' (which stands for Raising Tom Bright; but the full name doesn't need to be on the business card as it is more of a personal business name). To celebrate the new business I would like to get him some business cards made.
I would like the business name to be listed as 'RTB' and somewhere on the card I would like 'Sydney wide removals and relocation services'. I would like it to be obvious from the front of the card that it is a removalist business card. If a truck or some other feature that makes it look like a removalist business card could added it would be appreciated.
I don't mind what colours are used, but I would like the colour blue to feature somewhere in the design. It can be bright and fun, which is how Tom was.
I will also need the company's email address and phone number listed
The email address is: rtbremovals@quillpost.example
The contact number is: 0417 282 934
I don't need a contact name listed on the card, but perhaps 'Owned and operated by the Pendleworth family' could be added near the contact details in small font.
Thank you very much for considering this project!
Kind regards,
Fiona
Updates
Could you please change the mobile contact number to 0417 282 934. This is the only contact phone number required on the card now.
Thank you!

```html
<!DOCTYPE html>
<html lang="en">
<head>
<meta charset="utf-8">
<title>RTB Removals – Business Card</title>
<link rel="stylesheet" href="https://fonts.googleapis.com/css2?family=Open+Sans:wght@400&family=Nanum+Pen+Script&display=swap">
<style>
  :root {
    --kraft-light: #cfae86;
    --kraft-mid: #c6a47b;
    --kraft-dark: #bb9870;
    --brand-blue: #1d9be0;
    --ink: #1b1b1b;
    --rule: #6b5a48;
    --icon-fg: #ffffff;
  }
  html, body {
    margin: 0;
    padding: 0;
    width: 686px;
    height: 1200px;
    overflow: hidden;
    background: var(--kraft-mid);
  }
  .card {
    position: relative;
    width: 686px;
    height: 1200px;
    overflow: hidden;
    font-family: "Open Sans", Arial, sans-serif;
    color: var(--ink);
  }
  .card__paper {
    position: absolute;
    inset: 0;
    background: radial-gradient(ellipse at 40% 30%, var(--kraft-light) 0%, var(--kraft-mid) 55%, var(--kraft-dark) 100%);
  }
  .brand {
    position: absolute;
    left: 0;
    right: 0;
    top: 92px;
    text-align: center;
    color: var(--brand-blue);
    font-weight: 400;
  }
  .brand__name {
    display: block;
    font-size: 300px;
    line-height: 330px;
    letter-spacing: 6px;
  }
  .brand__service {
    display: block;
    margin-top: 10px;
    font-size: 104px;
    line-height: 120px;
    letter-spacing: 4px;
  }
  .tagline {
    position: absolute;
    left: 0;
    right: 0;
    top: 650px;
    text-align: center;
    font-family: "Nanum Pen Script", cursive;
    font-size: 40px;
    color: var(--brand-blue);
  }
  .contact {
    position: absolute;
    left: 160px;
    top: 846px;
    height: 324px;
    border-left: 2px solid var(--rule);
  }
  .contact__services {
    margin: 0;
    padding: 8px 0 0 20px;
    font-size: 34px;
    line-height: 46px;
    letter-spacing: 0.2px;
    text-transform: uppercase;
  }
  .contact__item {
    position: absolute;
    left: 20px;
    font-size: 31px;
    white-space: nowrap;
  }
  .contact__item--email { top: 104px; }
  .contact__item--phone { top: 184px; }
  .contact__icon {
    position: absolute;
    left: -68px;
    width: 54px;
    height: 54px;
  }
  .contact__item--email .contact__icon { top: -6px; }
  .contact__item--phone .contact__icon { top: -10px; }
</style>
</head>
<body>
<main class="card">
  <div class="card__paper" role="img" aria-label="Kraft paper texture background"></div>

  <h1 class="brand">
    <span class="brand__name">RTB</span>
    <span class="brand__service">REMOVALS</span>
  </h1>

  <p class="tagline">Owned &amp; operated by the Pendleworth family</p>

  <section class="contact">
    <p class="contact__services">Sydney wide removals +<br>relocation services</p>

    <div class="contact__item contact__item--email">
      <svg class="contact__icon" viewBox="0 0 54 54" aria-hidden="true">
        <circle cx="27" cy="27" r="27" fill="var(--ink)"/>
        <rect x="13" y="17" width="28" height="20" fill="none" stroke="var(--icon-fg)" stroke-width="2.5"/>
        <polyline points="13,17 27,29 41,17" fill="none" stroke="var(--icon-fg)" stroke-width="2.5"/>
      </svg>
      rtbremovals@quillpost.example
    </div>

    <div class="contact__item contact__item--phone">
      <svg class="contact__icon" viewBox="0 0 54 54" aria-hidden="true">
        <circle cx="27" cy="27" r="27" fill="var(--ink)"/>
        <path d="M12 22 Q27 10 42 22 L38 26 L33 22 L21 22 L16 26 Z" fill="var(--icon-fg)"/>
        <path d="M19 27 L35 27 L39 40 L15 40 Z" fill="var(--icon-fg)"/>
        <circle cx="27" cy="33" r="3.5" fill="var(--ink)"/>
      </svg>
      0417 282 934
    </div>
  </section>
</main>
</body>
</html>
```